We need motivational posters designed to be used in classrooms at a truck driving school. The purpose of the posters is to motivate the students.

I want the the quotes to be the main focal point of emphasis and our logo on the bottom of the poster for branding purposes.

I would like the images to be related to the trucking industry

Below are the quotes for the posters

Poster 1
"Start where you are. Use what you have. Do what you can."
-Dorian Vell-

Poster 2
"The secret of getting ahead is getting started"
-Lewis Crane-

Poster 3
"Most effective way to do it, is to do it."
-Odessa Brindle-

Poster 4
"Set your goals big, and don't stop till you get there."
-Cy Morrow-

Poster 5
"If you are not willing to learn, no one can help you. If you are determined to learn, no one can stop you."
-Unknown-

Poster 6
"The will to succeed is important, but what's more important is the will to prepare."
-Teddy Sloane-

THESE POSTERS SHOULD BE DESIGNED AS 18X24
LANDSCAPE AND PORTRAIT ORIENTATION

```html
<!DOCTYPE html>
<html lang="en">
<head>
<meta charset="utf-8">
<title>Motivational Poster – Odessa Brindle</title>
<link rel="stylesheet" href="https://fonts.googleapis.com/css2?family=Alfa+Slab+One&family=Oswald:wght@600&display=swap">
<style>
  :root {
    --paper: #ffffff;
    --ink: #1a1a1a;
    --gold: #fdb913;
    --frame-dark: #111111;
  }
  html, body {
    margin: 0;
    padding: 0;
    width: 934px;
    height: 1200px;
    overflow: hidden;
    background: var(--paper);
  }
  .poster {
    display: block;
    width: 934px;
    height: 1200px;
  }
  .frame-outer { fill: none; stroke: var(--frame-dark); stroke-width: 14; }
  .frame-inner { fill: none; stroke: var(--gold); stroke-width: 10; }
  .quote {
    font-family: "Alfa Slab One", "Rockwell", serif;
    text-transform: uppercase;
  }
  .quote--ink { fill: var(--ink); }
  .quote--gold { fill: var(--gold); }
  .attribution {
    font-family: "Oswald", "Arial Narrow", sans-serif;
    font-weight: 600;
    fill: var(--ink);
    text-transform: uppercase;
  }
  .brand-mark { fill: var(--gold); }
  .brand-name {
    font-family: "Oswald", "Arial Narrow", sans-serif;
    font-weight: 600;
    fill: var(--ink);
    text-transform: uppercase;
  }
</style>
</head>
<body>
<svg class="poster" viewBox="0 0 934 1200" xmlns="http://www.w3.org/2000/svg" role="img" aria-label="The most effective way to do it, is to do it. — Odessa Brindle">
  <rect class="frame-outer" x="94" y="86" width="785" height="1045"/>
  <rect class="frame-inner" x="113" y="105" width="747" height="1007"/>

  <g class="quote-block">
    <text class="quote quote--ink" x="137" y="262" font-size="80" textLength="189" lengthAdjust="spacingAndGlyphs">The</text>
    <text class="quote quote--gold" x="343" y="283" font-size="185" textLength="463" lengthAdjust="spacingAndGlyphs">Most</text>
    <text class="quote quote--ink" x="231" y="386" font-size="98" textLength="489" lengthAdjust="spacingAndGlyphs">Effective</text>
    <text class="quote quote--ink" x="369" y="480" font-size="110" textLength="222" lengthAdjust="spacingAndGlyphs">Way</text>
    <text class="quote quote--ink" x="206" y="592" font-size="134" textLength="557" lengthAdjust="spacingAndGlyphs">To Do It,</text>
    <text class="quote quote--ink" x="437" y="694" font-size="86" textLength="86" lengthAdjust="spacingAndGlyphs">Is</text>
    <text class="quote quote--gold" x="283" y="840" font-size="172" textLength="420" lengthAdjust="spacingAndGlyphs">To Do</text>
    <text class="quote quote--gold" x="377" y="977" font-size="172" textLength="206" lengthAdjust="spacingAndGlyphs">It.</text>
  </g>

  <text class="attribution" x="154" y="1083" font-size="50" textLength="326" lengthAdjust="spacingAndGlyphs">-Odessa Brindle</text>

  <g class="brand">
    <circle class="brand-mark" cx="662" cy="1050" r="27"/>
    <text class="brand-name" x="698" y="1046" font-size="30" textLength="133" lengthAdjust="spacingAndGlyphs">Northline</text>
    <text class="brand-name" x="698" y="1070" font-size="15" textLength="133" lengthAdjust="spacingAndGlyphs">Truck Driving School</text>
  </g>
</svg>
</body>
</html>
```